Vitalquorra.com

I need a web design for a Online Wellness Center based in Chicago, IL and it's called "Vitalquorra" We provide Health risk assessment to individuals and interventions. Our portal has a Health Activity tracker where our members record health activities and aerobic miles and biometric data. Our Online wellness center tracks the participant's progress toward health goals and awards points for completed activities.
I started working on this website but the designer was not able to designer a website which describes what we do. I need a fresh look on this project. I need a very attractive, responsive website which says what we do.
These are the things we do.
1. We provide Health Risk Assessments to individuals and Co-operations
2. We Provide Free health screenings to undeserved communities
3. Assist individuals access free or affordable medications
4. We ask providers/doctors to see (or do a complete physical) one individual free of charge once a year (those individuals who are no insured and don't have money to pay from their pocket)
5. Assist patient access lab work at low cost
Our goal is to provide services that will lower the cost of care for our members.

Here is the website: www.vitalquorra.com still underdevelopment. PLEASE DO NOT COPY THIS STYLE OF WEBSITE. IT'S A BAD DESIGN AND THAT IS WHY I'M RE-DESIGNING THE SITE

Target Market(s)

Health individuals between the age of 21 to 65 Plus years old. Insured and uninsured

Industry/Entity Type

Health And Wellness

Coding

Coded - Design and coding required

Number of Pages Required

5+ page

Colors
0292cd

Requirements
Must have
• I'm still working on this websiteHere is the menu: Home, About us, Services, Health Screening, Providers, Contacts
• Please see. www.vitalquorra.com
Nice to have
• Event calender
• Upcoming Event
• Medication
• Lab assist
• Providers/Free Clinics

```html
<!DOCTYPE html>
<html lang="en">
<head>
<meta charset="utf-8">
<title>Vitalquorra – Online Wellness Center</title>
<link href="https://fonts.googleapis.com/css2?family=Open+Sans:wght@400;600;700;800&display=swap" rel="stylesheet">
<style>
:root{
  --green:#7ab929;
  --green-dark:#5f9a1a;
  --blue:#0292cd;
  --navy:#2b3a42;
  --ink:#333b40;
  --muted:#6b7479;
  --line:#dfe3e6;
  --white:#ffffff;
  --footer:#262c30;
}
*{box-sizing:border-box;margin:0;padding:0}
html,body{width:774px;height:1200px;overflow:hidden;background:var(--white)}
body{font-family:"Open Sans",Arial,sans-serif;color:var(--ink);position:relative}

.site-header{height:44px;display:flex;align-items:center;padding:0 18px;justify-content:space-between}
.brand{display:flex;align-items:center;gap:6px;font-size:24px;font-weight:700;color:var(--green)}
.brand-dot{width:18px;height:18px;border-radius:50%;background:var(--blue)}
.header-address{font-size:7.5px;color:var(--muted);line-height:1.35;margin-left:40px}
.header-phone{display:flex;align-items:center;gap:6px;font-size:17px;font-weight:600;color:var(--blue)}

.main-nav{height:26px;background:var(--navy);display:flex;padding-left:18px}
.main-nav a{color:var(--white);font-size:8px;font-weight:600;text-decoration:none;display:flex;align-items:center;padding:0 22px;letter-spacing:.3px}
.main-nav a.active{background:var(--green)}

.hero{position:relative;height:282px;overflow:hidden}
.hero-photo{position:absolute;inset:0;background:linear-gradient(90deg,#e9eef0 0%,#d8e0e3 35%,#b9c4c9 60%,#8d9ba3 100%)}
.hero-text{position:absolute;left:398px;top:78px;color:var(--white)}
.hero-title{font-size:32px;font-weight:400;line-height:1.05;text-shadow:0 1px 3px rgba(0,0,0,.25)}
.hero-sub{font-size:20px;font-weight:700;margin-top:6px;text-shadow:0 1px 3px rgba(0,0,0,.25)}
.hero-btn{display:inline-block;margin-top:20px;background:var(--navy);color:var(--white);font-size:9px;font-weight:700;padding:9px 14px;letter-spacing:.3px}

.benefits{position:absolute;left:18px;top:368px;width:346px}
.section-title{font-size:19px;font-weight:800;line-height:1.1;color:var(--ink)}
.section-kicker{font-size:8px;font-weight:700;color:var(--green);margin-top:4px;text-transform:uppercase}
.benefit-list{list-style:none;margin-top:8px}
.benefit-list li{display:flex;gap:6px;font-size:7.8px;line-height:1.35;margin-bottom:5px;color:var(--ink)}
.benefit-list svg{flex:none;margin-top:1px}

.schedule{position:absolute;left:380px;top:386px;width:376px}
.schedule-head{height:30px;background:var(--blue);display:flex;align-items:center;justify-content:space-between;padding:0 8px 0 12px}
.schedule-head h2{color:var(--white);font-size:14px;font-weight:600}
.create-btn{background:var(--green);color:var(--white);font-size:7.5px;font-weight:700;padding:6px 8px;text-transform:uppercase}
.cal-bar{display:flex;align-items:center;justify-content:space-between;padding:6px 4px}
.cal-nav{display:flex;gap:2px}
.cal-nav span,.cal-views span{border:1px solid var(--line);font-size:7px;padding:2px 5px;color:var(--muted)}
.cal-month{font-size:16px;color:var(--ink)}
.cal-views{display:flex;gap:1px}
.calendar{width:100%;border-collapse:collapse;table-layout:fixed}
.calendar th{font-size:7px;font-weight:600;border:1px solid var(--line);padding:2px;background:#f4f5f6}
.calendar td{border:1px solid var(--line);height:27px;vertical-align:top;font-size:7px;padding:2px 3px;text-align:right;color:var(--muted);position:relative}
.calendar td.other{color:#b7bdc1}
.calendar td.today{background:#fcf8e3}
.cal-event{position:absolute;left:1px;right:1px;bottom:3px;height:6px;background:var(--blue);border-radius:1px}

.events{position:absolute;left:18px;top:604px;width:346px}
.events .section-title{font-size:17px}
.event-row{display:flex;gap:16px;margin-top:6px}
.event{width:165px}
.event-name{font-size:8px;font-weight:700;text-transform:uppercase}
.event-date{font-size:18px;font-weight:600;color:var(--green);line-height:1.2}
.event-body{display:flex;gap:6px;margin-top:3px}
.event-thumb{width:40px;height:30px;flex:none;background:linear-gradient(135deg,#c9d3d8,#8e9ea6)}
.event-body p{font-size:7px;line-height:1.3;color:var(--muted)}

.tiles{position:absolute;left:18px;top:734px;width:738px;display:flex;gap:18px}
.tile{flex:1;height:106px;position:relative;display:flex;align-items:center;justify-content:center}
.tile-clinics{background:linear-gradient(120deg,#5c6d75,#9aa8ae 60%,#6d7d84)}
.tile-lab{background:linear-gradient(120deg,#4d6f7d,#93b0bb 55%,#5f7e8a)}
.tile span{color:var(--white);font-size:20px;font-weight:400;letter-spacing:.5px;text-shadow:0 1px 3px rgba(0,0,0,.4)}

.care{position:absolute;left:0;top:856px;width:774px;height:290px}
.care-shape{position:absolute;inset:0}
.care-list{position:absolute;left:44px;top:36px;list-style:none}
.care-list li{display:flex;align-items:center;gap:14px;height:76px}
.care-icon{width:44px;height:44px;border-radius:50%;border:2px solid var(--white);display:flex;align-items:center;justify-content:center;flex:none}
.care-list h3{color:var(--white);font-size:16px;font-weight:400}
.care-list p{color:#eaf5dc;font-size:7px;line-height:1.35;width:260px;margin-top:2px}
.care-photo{position:absolute;right:48px;top:22px;width:190px;height:268px;background:linear-gradient(180deg,#e6eaec,#c4ccd0)}

.site-footer{position:absolute;left:0;bottom:0;width:774px;height:42px;background:var(--footer);display:flex;align-items:center;padding:0 18px;gap:8px}
.email-field{width:130px;height:18px;background:var(--white);font-size:7px;color:var(--muted);display:flex;align-items:center;padding-left:6px}
.subscribe{height:18px;background:var(--navy);color:var(--white);font-size:7px;padding:0 12px;display:flex;align-items:center;border:1px solid #4a5962}
.copyright{font-size:6.5px;color:#aab2b6;margin-left:70px}
.social{display:flex;gap:5px;margin-left:auto}
.social span{width:14px;height:14px;border-radius:50%;background:#e8ecee}
</style>
</head>
<body>

<header class="site-header">
  <div class="brand"><span class="brand-dot"></span>Vitalquorra</div>
  <div class="header-address">Vitalquorra 418 Lakeview Avenue<br>Marlow Falls, 00417 | (555) 010-2211</div>
  <div class="header-phone">
    <svg width="16" height="16" viewBox="0 0 24 24"><circle cx="12" cy="12" r="12" fill="#7ab929"/><path d="M8.5 6.5l2 0 1 3-1.4 1.1a7 7 0 003.3 3.3l1.1-1.4 3 1v2a1.5 1.5 0 01-1.6 1.5A10 10 0 017 8.1 1.5 1.5 0 018.5 6.5z" fill="#fff"/></svg>
    1-555-010-2211
  </div>
</header>

<nav class="main-nav">
  <a class="active">HOME</a><a>ABOUT US</a><a>SERVICES</a><a>HEALTH SCREENING</a><a>PROVIDERS</a><a>CONTACTS</a>
</nav>

<section class="hero">
  <div class="hero-photo" role="img" aria-label="Photo of a smiling female doctor and male doctor in white coats"></div>
  <div class="hero-text">
    <h1 class="hero-title">Do you know your<br>risk factor?</h1>
    <p class="hero-sub">We you know about risk factor?</p>
    <span class="hero-btn">LEARN YOUR RISK</span>
  </div>
</section>

<section class="benefits">
  <h2 class="section-title">BENEFITS OF OUR WELLNESS<br>SERVICES</h2>
  <p class="section-kicker">These are the things we do</p>
  <ul class="benefit-list">
    <li><svg width="8" height="8" viewBox="0 0 10 10"><path d="M1 5l3 3 5-6" stroke="#7ab929" stroke-width="2" fill="none"/></svg>We provide Health Risk Assessments to individuals and Co-operations</li>
    <li><svg width="8" height="8" viewBox="0 0 10 10"><path d="M1 5l3 3 5-6" stroke="#7ab929" stroke-width="2" fill="none"/></svg>We Provide Free health screenings to undeserved communities</li>
    <li><svg width="8" height="8" viewBox="0 0 10 10"><path d="M1 5l3 3 5-6" stroke="#7ab929" stroke-width="2" fill="none"/></svg>Assist individuals access free or affordable medications</li>
    <li><svg width="8" height="8" viewBox="0 0 10 10"><path d="M1 5l3 3 5-6" stroke="#7ab929" stroke-width="2" fill="none"/></svg>We ask providers/doctors to see (or do a complete physical) one individual free of charge once a year (those individuals who are not insured and don't have money to pay from their pocket)</li>
    <li><svg width="8" height="8" viewBox="0 0 10 10"><path d="M1 5l3 3 5-6" stroke="#7ab929" stroke-width="2" fill="none"/></svg>Assist patient access lab work at low cost. Our goal is to provide services that will lower the cost of care for our members.</li>
  </ul>
</section>

<section class="schedule">
  <div class="schedule-head"><h2>Our Screening Schedule</h2><span class="create-btn">Create your event</span></div>
  <div class="cal-bar">
    <div class="cal-nav"><span>&lsaquo;</span><span>&rsaquo;</span><span>today</span></div>
    <div class="cal-month">September 2015</div>
    <div class="cal-views"><span>month</span><span>week</span><span>day</span></div>
  </div>
  <table class="calendar">
    <tr><th>Sun</th><th>Mon</th><th>Tue</th><th>Wed</th><th>Thu</th><th>Fri</th><th>Sat</th></tr>
    <tr><td class="other">30</td><td class="other">31</td><td>1</td><td>2</td><td>3</td><td>4</td><td>5</td></tr>
    <tr><td>6</td><td>7</td><td>8</td><td>9</td><td>10</td><td>11</td><td>12</td></tr>
    <tr><td>13</td><td>14</td><td class="today">15<span class="cal-event"></span></td><td>16</td><td>17</td><td>18</td><td>19</td></tr>
    <tr><td>20<span class="cal-event"></span></td><td>21<span class="cal-event"></span></td><td>22<span class="cal-event"></span></td><td>23</td><td>24</td><td>25<span class="cal-event"></span></td><td>26</td></tr>
    <tr><td>27<span class="cal-event"></span></td><td>28<span class="cal-event"></span></td><td>29</td><td>30</td><td class="other">1</td><td class="other">2</td><td class="other">3</td></tr>
  </table>
</section>

<section class="events">
  <h2 class="section-title">UPCOMING EVENT</h2>
  <div class="event-row">
    <div class="event">
      <p class="event-name">Event title goes here</p>
      <p class="event-date">11/05/15</p>
      <div class="event-body"><div class="event-thumb" role="img" aria-label="Event photo"></div><p>Brindlewood Health Circle is a group of Internal Medicine Physicians</p></div>
    </div>
    <div class="event">
      <p class="event-name">Event title goes here</p>
      <p class="event-date">30/08/15</p>
      <div class="event-body"><div class="event-thumb" role="img" aria-label="Event photo"></div><p>Brindlewood Health Circle is a group of Internal Medicine Physicians</p></div>
    </div>
  </div>
</section>

<section class="tiles">
  <div class="tile tile-clinics" role="img" aria-label="Photo of a doctor with a patient at a free clinic"><span>FREE CLINICS</span></div>
  <div class="tile tile-lab" role="img" aria-label="Photo of laboratory test tubes"><span>LAB ASSIST</span></div>
</section>

<section class="care">
  <svg class="care-shape" viewBox="0 0 774 290" preserveAspectRatio="none">
    <path d="M0 40 Q300 -10 774 20 L774 290 L0 290 Z" fill="#7ab929"/>
    <path d="M0 52 Q300 2 774 32" stroke="#5f9a1a" stroke-width="3" fill="none"/>
  </svg>
  <ul class="care-list">
    <li>
      <span class="care-icon"><svg width="20" height="20" viewBox="0 0 24 24"><path d="M3 12h4l2-5 4 10 2-5h6" stroke="#fff" stroke-width="2" fill="none"/></svg></span>
      <div><h3>Follow up care</h3><p>We stay in touch after every visit, review your results and help you plan the next healthy steps toward your goals.</p></div>
    </li>
    <li>
      <span class="care-icon"><svg width="20" height="20" viewBox="0 0 24 24"><circle cx="12" cy="8" r="4" stroke="#fff" stroke-width="2" fill="none"/><path d="M4 21c1-5 15-5 16 0" stroke="#fff" stroke-width="2" fill="none"/></svg></span>
      <div><h3>Physicals</h3><p>Partner doctors offer one complete yearly physical free of charge for members who have no insurance coverage.</p></div>
    </li>
    <li>
      <span class="care-icon"><svg width="20" height="20" viewBox="0 0 24 24"><path d="M5 19l9-9M11 7l6 6M14 4l6 6M4 20l2-2" stroke="#fff" stroke-width="2" fill="none"/></svg></span>
      <div><h3>Immunizations</h3><p>Seasonal flu shots and routine vaccines are available at low cost through our community clinic partners.</p></div>
    </li>
  </ul>
  <div class="care-photo" role="img" aria-label="Photo of a smiling senior doctor with a stethoscope"></div>
</section>

<footer class="site-footer">
  <div class="email-field">Enter your email</div>
  <div class="subscribe">Subscribe</div>
  <p class="copyright">© Copyright 2015, All Rights Reserved by vitalquorra</p>
  <div class="social"><span></span><span></span><span></span><span></span></div>
</footer>

</body>
</html>
```